Door Sticker for Loyalty Rewards App

We need to make stickers that will go on the door of the merchants who are part of the Quiver app.

I have attached the Quiver logo, our colours and examples of other door stickers.

Target Market(s)

Millennials

Colors

Designer to choose colors to be used in the design.

Requirements
Must have
• We would like the Quiver logo as the biggest part of the sticker with the text "Effortless Rewards Available Here" and our URL: www.TrulyQuiverTime.com (you can drop the www if you want).
• Must use the Quiver colours.

```html
<!DOCTYPE html>
<html lang="en">
<head>
<meta charset="utf-8">
<title>Quiver Door Sticker</title>
<link rel="stylesheet" href="https://fonts.googleapis.com/css2?family=Montserrat:wght@500;600;700&display=swap">
<style>
  :root {
    --bg: #eceef1;
    --sticker-fill: #ffffff;
    --brand-pink: #dc5a98;
    --brand-blue: #4a86bd;
    --brand-purple: #7a57a3;
    --ink-navy: #3d3b6b;
    --url-blue: #3f7ab8;
  }
  html, body {
    margin: 0;
    padding: 0;
    width: 1200px;
    height: 858px;
    overflow: hidden;
    background: var(--bg);
  }
  .door-sticker {
    display: block;
    width: 1200px;
    height: 858px;
  }
  .sticker-outline { fill: var(--sticker-fill); stroke: #ffffff; stroke-width: 26; stroke-linejoin: round; }
  .sticker-body { fill: var(--sticker-fill); stroke: var(--brand-pink); stroke-width: 11; stroke-linejoin: round; }
  .accent-line { fill: none; stroke-width: 7; stroke-linecap: round; }
  .accent-line--blue { stroke: var(--brand-blue); }
  .accent-line--purple { stroke: var(--brand-purple); }
  .accent-dot--blue { fill: var(--brand-blue); stroke: #fff; stroke-width: 3; }
  .accent-dot--pink { fill: var(--brand-pink); stroke: #fff; stroke-width: 3; }
  .accent-triangle--blue { fill: var(--brand-blue); stroke: #fff; stroke-width: 3; stroke-linejoin: round; }
  .accent-triangle--purple { fill: var(--brand-purple); stroke: #fff; stroke-width: 3; stroke-linejoin: round; }
  .tagline {
    font-family: "Montserrat", sans-serif;
    font-weight: 600;
    font-size: 22px;
    fill: var(--ink-navy);
  }
  .brand-name {
    font-family: "Montserrat", sans-serif;
    font-weight: 700;
    font-size: 78px;
    fill: var(--ink-navy);
  }
  .brand-square { fill: var(--brand-pink); }
  .site-url {
    font-family: "Montserrat", sans-serif;
    font-weight: 500;
    font-size: 20px;
    fill: var(--url-blue);
  }
</style>
</head>
<body>
<svg class="door-sticker" viewBox="0 0 1200 858" xmlns="http://www.w3.org/2000/svg" role="img" aria-label="Quiver door sticker: Effortless Rewards Available Here, trulyquivertime.com">
  <g class="decor">
    <line class="accent-line accent-line--blue" x1="430" y1="240" x2="730" y2="212"/>
    <circle class="accent-dot--blue" cx="762" cy="205" r="11"/>
    <circle class="accent-dot--pink" cx="798" cy="202" r="11"/>
    <line class="accent-line accent-line--purple" x1="856" y1="302" x2="810" y2="574"/>
    <polygon class="accent-triangle--blue" points="305,445 378,390 385,470"/>
    <polygon class="accent-triangle--purple" points="343,533 365,492 385,527"/>
  </g>

  <g class="sticker">
    <path class="sticker-outline" d="M 425 268 L 812 236 Q 848 233 841 270 L 792 556 Q 786 586 754 588 L 680 594 Q 650 598 640 625 L 625 676 Q 620 692 610 678 L 600 642 Q 594 620 570 618 L 460 610 Q 432 608 428 580 L 400 300 Q 397 270 425 268 Z"/>
    <path class="sticker-body" d="M 425 268 L 812 236 Q 848 233 841 270 L 792 556 Q 786 586 754 588 L 680 594 Q 650 598 640 625 L 625 676 Q 620 692 610 678 L 600 642 Q 594 620 570 618 L 460 610 Q 432 608 428 580 L 400 300 Q 397 270 425 268 Z"/>
  </g>

  <g class="sticker-content">
    <text class="tagline" x="620" y="298" text-anchor="middle" transform="rotate(-3 620 298)">Effortless Rewards Available Here</text>
    <rect class="brand-square" x="462" y="390" width="34" height="34" rx="4"/>
    <text class="brand-name" x="510" y="430">Quiver</text>
    <text class="site-url" x="605" y="533" text-anchor="middle">trulyquivertime.com</text>
  </g>
</svg>
</body>
</html>
```